Veranta - Solution provider in business consulting

Veranta is a swiss based company providing solutions for developing markets. The business covers various fields of business consulting, such as supply chain, product costs, quality management and manufacturing management. The Business operates in a efficient, straight and solution oriented manner.
The final design should communicate these characteristics. Asian people as well as as western people shall identify the qualities of the company at first sight.
The customer needs business cards with a simple view but an recognizable design, printed in high quality. Engraved elements such as the globe or simple words are possible.
Available colors are: (RAL)
102/102/102
51/102/102
153/204/153
255/102/51
Font: Calibri
Industry/Entity Type
Business
Look and feel
Each slider illustrates characteristics of the customer's brand and the style your logo design should communicate.

```html
<!DOCTYPE html>
<html lang="en">
<head>
<meta charset="utf-8">
<title>Veranta – Business Card</title>
<link rel="stylesheet" href="https://fonts.googleapis.com/css2?family=Open+Sans:wght@400;600;700&display=swap">
<style>
  :root {
    --backdrop: #d9d6d1;
    --paper: #f4f3ef;
    --ink: #666666;
    --ink-dark: #5a5a5a;
    --art-light: #8c8c8c;
    --art-dark: #6a6a6a;
  }
  html, body {
    margin: 0;
    width: 1200px;
    height: 800px;
    overflow: hidden;
    background: var(--backdrop);
    font-family: "Open Sans", Calibri, Arial, sans-serif;
  }
  .card {
    position: absolute;
    left: 150px;
    top: 140px;
    width: 900px;
    height: 520px;
    background: var(--paper);
    overflow: hidden;
    box-shadow: 0 6px 18px rgba(0,0,0,0.18);
    color: var(--ink);
  }
  .feature-art {
    position: absolute;
    left: 40px;
    top: 95px;
    width: 390px;
    height: 390px;
    background: linear-gradient(180deg, var(--art-light), var(--art-dark));
  }
  .brand {
    position: absolute;
    right: 60px;
    top: 42px;
    display: flex;
    align-items: center;
    gap: 14px;
    font-size: 44px;
    font-weight: 400;
    color: var(--ink);
    letter-spacing: 0.5px;
    line-height: 1;
  }
  .brand-dot {
    width: 34px;
    height: 34px;
    border-radius: 50%;
    background: var(--ink);
  }
  .rule {
    position: absolute;
    left: 440px;
    right: 0;
    top: 122px;
    height: 2px;
    background: var(--ink);
  }
  .identity {
    position: absolute;
    right: 60px;
    top: 138px;
    text-align: right;
  }
  .identity .name {
    font-size: 28px;
    font-weight: 700;
    color: var(--ink-dark);
    letter-spacing: 0.5px;
    line-height: 1.2;
  }
  .identity .role {
    font-size: 17px;
    line-height: 1.3;
  }
  .contacts {
    position: absolute;
    right: 60px;
    top: 232px;
    list-style: none;
    margin: 0;
    padding: 0;
    font-size: 21px;
    line-height: 30px;
  }
  .contacts li {
    display: flex;
    justify-content: flex-end;
    align-items: center;
    gap: 12px;
  }
  .contacts svg {
    width: 20px;
    height: 20px;
    flex: none;
  }
  .address {
    position: absolute;
    right: 92px;
    top: 372px;
    text-align: right;
    font-size: 21px;
    line-height: 29px;
    font-style: normal;
  }
  .address .company {
    font-weight: 700;
    color: var(--ink-dark);
  }
</style>
</head>
<body>
  <article class="card">
    <div class="feature-art" role="img" aria-label="Engraved globe illustration in dark grey"></div>

    <div class="brand"><span class="brand-name">veranta</span><span class="brand-dot"></span></div>
    <div class="rule"></div>

    <div class="identity">
      <div class="name">MARCO KELLER</div>
      <div class="role">CEO</div>
    </div>

    <ul class="contacts">
      <li><span>+41 79 523 6180</span>
        <svg viewBox="0 0 20 20" aria-label="Phone"><rect width="20" height="20" rx="3" fill="#666"/><path d="M6 4.5c1 0 1.6 2.4 1.2 3-.4.6-1 .7-.6 1.6.6 1.2 1.5 2.1 2.7 2.7.9.4 1-.2 1.6-.6.6-.4 3 .2 3 1.2 0 1.2-1.3 2.4-2.6 2.2C7.8 14 5.9 12.1 5.3 8.6 5 7.2 5 4.5 6 4.5z" fill="#f4f3ef"/></svg></li>
      <li><span>+41 71 884 3172</span>
        <svg viewBox="0 0 20 20" aria-label="Fax"><rect width="20" height="20" rx="3" fill="#666"/><rect x="6" y="3.5" width="8" height="4" fill="#f4f3ef"/><rect x="3.5" y="8" width="13" height="6" rx="1" fill="#f4f3ef"/><rect x="6" y="12" width="8" height="4.5" fill="#f4f3ef" stroke="#666" stroke-width="1"/></svg></li>
      <li><span>marco.keller@veranta.ch</span>
        <svg viewBox="0 0 20 20" aria-label="Email"><rect width="20" height="20" rx="3" fill="#666"/><rect x="3.5" y="5.5" width="13" height="9" fill="#f4f3ef"/><path d="M3.5 5.5l6.5 5 6.5-5" fill="none" stroke="#666" stroke-width="1.3"/></svg></li>
      <li><span>www.veranta.ch</span>
        <svg viewBox="0 0 20 20" aria-label="Website"><rect width="20" height="20" rx="3" fill="#666"/><circle cx="10" cy="10" r="6.5" fill="none" stroke="#f4f3ef" stroke-width="1.3"/><ellipse cx="10" cy="10" rx="3" ry="6.5" fill="none" stroke="#f4f3ef" stroke-width="1.1"/><path d="M3.5 10h13M4.5 7h11M4.5 13h11" stroke="#f4f3ef" stroke-width="1.1"/></svg></li>
    </ul>

    <address class="address">
      <div class="company">Veranta GmbH</div>
      <div>Lindenweg 14</div>
      <div>8400 Winterthur, Switzerland</div>
    </address>
  </article>
</body>
</html>
```